New, modern business card for growing audiology practice

We need a new business card for our audiology practice. Our logo and website have recently changed (more modern) and we want our business cards to reflect this change.
We conduct hearing tests, perform earwax removals, and fit & dispense hearing aids to our patients. We are a family owned practice in which the owner is the one who works directly with the patient. I have attached logos in various formats to use, as well as two ideas I found on this website; as well as a scanned copy of our current logo. Good luck!

Industry/Entity Type

Business

Contact Information for Business Card

Company name: Maplow Hearing Center
Provider name: Peter Mulvoy, Au.D. F/ISN
Phone number: (555) 318-6042
Address: 87 W. Linden Ave. Brookmere Falls, OH 45017
email: maplowhearing@postvale.net
website: maplowhearing.com

Colors
000000
aaaaaa
dbdbdb
cacaca
9bcb3c
afd23c
cadf82
b1b1b1

Requirements
Must have
• My card must include information in the "details" section. In the attached images, I found a few that I liked and I would like to model after - "brisk tumblin'" and "Sound Wellness Center".
• Must be horizontal.
• Must include logos provided. I uploaded them in various file formats and various ways.
• Must match logo font, if possible, if not, please get as close as you can.
Nice to have
• I really like the idea of having a color on one side with just the logo and company name and the contact information and provider name on the other side. I also really like the idea of having the main color dominating on the logo/company side with accent of that same color on the contact side of the card.
Should not have
• Must not be vertical.

```html
<!DOCTYPE html>
<html lang="en">
<head>
<meta charset="utf-8">
<title>Maplow Hearing Center – Business Card</title>
<link rel="stylesheet" href="https://fonts.googleapis.com/css2?family=Lato:wght@400;700&display=swap">
<style>
  :root {
    --black: #000000;
    --green: #7cb342;
    --green-bright: #8cc63f;
    --paper: #f1f0ee;
    --paper-shade: #e4e3e1;
    --backdrop: #d9d6d2;
    --white: #ffffff;
    --divider: #5a8f2a;
  }
  * { box-sizing: border-box; margin: 0; padding: 0; }
  html, body {
    width: 1200px; height: 900px; overflow: hidden;
    background: var(--backdrop);
    font-family: "Lato", "Helvetica Neue", Arial, sans-serif;
  }
  .canvas {
    width: 1200px; height: 900px;
    display: flex; align-items: center; justify-content: center;
  }
  .business-card {
    width: 900px; height: 556px;
    display: flex; flex-direction: column;
    box-shadow: 0 10px 30px rgba(0,0,0,0.18);
  }
  .brand-panel {
    height: 266px;
    background: linear-gradient(180deg, var(--paper) 0%, var(--paper-shade) 100%);
    display: flex; align-items: center; justify-content: center;
    gap: 16px;
    padding-top: 26px;
  }
  .brand-dot {
    width: 26px; height: 26px; border-radius: 50%;
    background: var(--green);
    flex: none;
  }
  .brand-name {
    font-size: 46px; font-weight: 400; letter-spacing: 0.6px;
    color: var(--black); text-transform: uppercase; white-space: nowrap;
  }
  .accent-rule { height: 7px; background: var(--green-bright); }
  .contact-panel {
    flex: 1; background: var(--black); color: var(--white);
    display: flex; flex-direction: column; align-items: center;
    padding-top: 62px;
  }
  .provider { font-size: 20px; color: var(--white); white-space: nowrap; }
  .provider-name {
    font-size: 26px; font-weight: 700; color: var(--green-bright);
    text-transform: uppercase; letter-spacing: 0.3px;
  }
  .details { display: flex; margin-top: 24px; }
  .address {
    font-style: normal; text-align: right; font-size: 21px; line-height: 33px;
    padding: 6px 30px 6px 0; border-right: 2px solid var(--divider);
    white-space: nowrap;
  }
  .contact-list {
    list-style: none; padding-left: 30px;
    font-size: 21px; line-height: 33px; white-space: nowrap;
  }
  .contact-list li { display: flex; align-items: center; gap: 8px; }
  .contact-list svg { width: 18px; height: 18px; fill: var(--green-bright); flex: none; }
</style>
</head>
<body>
<main class="canvas">
  <section class="business-card">
    <header class="brand-panel">
      <span class="brand-dot"></span>
      <h1 class="brand-name">Maplow Hearing Center</h1>
    </header>
    <div class="accent-rule"></div>
    <div class="contact-panel">
      <p class="provider"><span class="provider-name">Peter Mulvoy</span>, AU.D. F/ISN</p>
      <div class="details">
        <address class="address">
          87 W. Linden<br>Ave. Brookmere Falls, OH 45017
        </address>
        <ul class="contact-list">
          <li>
            <svg viewBox="0 0 24 24" aria-hidden="true"><path d="M6.6 10.8a15.1 15.1 0 0 0 6.6 6.6l2.2-2.2c.3-.3.7-.4 1-.2 1.1.4 2.3.6 3.6.6.6 0 1 .4 1 1V20c0 .6-.4 1-1 1A17 17 0 0 1 3 4c0-.6.4-1 1-1h3.5c.6 0 1 .4 1 1 0 1.3.2 2.5.6 3.6.1.3 0 .7-.2 1z"/></svg>
            (555) 318-6042
          </li>
          <li>
            <svg viewBox="0 0 24 24" aria-hidden="true"><path d="M3 6h18l-9 7z"/><path d="M3 8l9 7 9-7v10H3z"/></svg>
            maplowhearing@postvale.net
          </li>
          <li>
            <svg viewBox="0 0 24 24" aria-hidden="true"><circle cx="12" cy="12" r="9"/><path d="M3 12h18M12 3c3 3 3 15 0 18M12 3c-3 3-3 15 0 18" stroke="#000" stroke-width="1.4" fill="none"/></svg>
            www.maplowhearing.com
          </li>
        </ul>
      </div>
    </div>
  </section>
</main>
</body>
</html>
```